Web Design Business Card

I need a new business card designed, we recently rebranded and I need to get a fresh design to match our new logo, colours and branding.

Details:

Dorian Keeble | Founder & CEO
Address: 7 Fernhollow Lane, #04-09 Maplecrest Vale, Singapore 583104
Tel: +65 93468120
Web: www.plumtrove.com.sg
hello@plumtrove.com.sg

I've attached my old card as well

Requirements
Must have
• Front and Back
Interesting use of logo
Correct use of colour scheme

```html
<!DOCTYPE html>
<html lang="en">
<head>
<meta charset="utf-8">
<title>Plumtrove Business Card – Front and Back</title>
<link href="https://fonts.googleapis.com/css2?family=Nunito+Sans:wght@400;700&display=swap" rel="stylesheet">
<style>
  :root {
    --page: #ffffff;
    --card-border: #8c8c8c;
    --ink: #6b625d;
    --accent: #1ea8e3;
    --label: #222222;
    --sky-deep: #0eaeee;
    --sky-light: #8ad9fd;
    --badge-top: #1ba6e8;
    --badge-bottom: #86d6fb;
    --white: #ffffff;
  }
  * { margin: 0; padding: 0; box-sizing: border-box; }
  html, body {
    width: 1200px;
    height: 472px;
    overflow: hidden;
    background: var(--page);
    font-family: "Nunito Sans", Arial, sans-serif;
  }
  .canvas {
    position: relative;
    width: 1200px;
    height: 472px;
  }
  .card {
    position: absolute;
    top: 50px;
    width: 497px;
    height: 302px;
  }
  .card--front {
    left: 45px;
    border: 1px solid var(--card-border);
    background: var(--white);
  }
  .card--back {
    left: 659px;
    background: linear-gradient(160deg, var(--sky-deep) 0%, var(--sky-light) 100%);
  }
  .side-label {
    position: absolute;
    font-size: 13px;
    letter-spacing: 0.5px;
    color: var(--label);
    transform: translateX(-50%);
  }
  .side-label--front { left: 291px; top: 370px; }
  .side-label--back { left: 907px; top: 364px; }

  .brand {
    position: absolute;
    left: 40px;
    top: 48px;
    display: flex;
    align-items: center;
  }
  .brand__dot {
    width: 72px;
    height: 72px;
    border-radius: 50%;
    background: linear-gradient(160deg, var(--badge-top), var(--badge-bottom));
    margin-right: 10px;
  }
  .brand__name {
    font-size: 42px;
    font-weight: 700;
    color: var(--ink);
    letter-spacing: -0.5px;
    line-height: 1;
    margin-top: -10px;
  }

  .contact {
    position: absolute;
    left: 122px;
    top: 134px;
    font-size: 14.5px;
    line-height: 20px;
    color: var(--ink);
  }
  .contact__person { margin-bottom: 18px; font-size: 15px; }
  .contact__name { color: var(--accent); text-transform: uppercase; }
  .contact__label { color: var(--accent); }

  .back-name {
    position: absolute;
    left: 48px;
    top: 140px;
    font-size: 40px;
    font-weight: 700;
    color: var(--white);
    letter-spacing: -0.5px;
  }
  .back-web {
    position: absolute;
    left: 268px;
    top: 235px;
    font-size: 16px;
    color: var(--white);
  }
</style>
</head>
<body>
<main class="canvas">
  <section class="card card--front" aria-label="Card front">
    <div class="brand">
      <span class="brand__dot" aria-hidden="true"></span>
      <span class="brand__name">plumtrove</span>
    </div>
    <div class="contact">
      <p class="contact__person"><span class="contact__name">Dorian Keeble</span> Founder &amp; CEO</p>
      <p>7 Fernhollow Lane,</p>
      <p>#04-09 Maplecrest Vale, Singapore 583104</p>
      <p><span class="contact__label">Tel:</span> +65 93468120</p>
      <p><span class="contact__label">Web:</span> www.plumtrove.com.sg</p>
      <p><span class="contact__label">Email:</span> hello@plumtrove.com.sg</p>
    </div>
  </section>
  <p class="side-label side-label--front">FRONT</p>

  <section class="card card--back" aria-label="Card back">
    <span class="back-name">plumtrove</span>
    <span class="back-web">www.plumtrove.com.sg</span>
  </section>
  <p class="side-label side-label--back">BACK</p>
</main>
</body>
</html>
```